General contractor/GM consaltant business card

I need a card for my contracting company in North Dakota, we build industrial buildings for the oil feild and oil feild related companies offices, shops, airplain hangars, airports ext. We have a familly atmosphere on the job and are very relational and personal.
Industry/Entity Type
Industrial
Contact Information for Business Card
Hollowpine Crafters LLC.
Dale T.Voskuijl
4873 Quenwick dr. Colorado Springs, CO. 80462
Cell# 406-738-1452
dale@hollowpinecrafters.example

```html
<!DOCTYPE html>
<html lang="en">
<head>
<meta charset="utf-8">
<title>Hollowpine Crafters LLC. — Business Card</title>
<link rel="stylesheet" href="https://fonts.googleapis.com/css2?family=Open+Sans:wght@400;600&family=Roboto:wght@500;700&display=swap">
<style>
  :root {
    --stage: #e9e7e3;
    --card-white: #ffffff;
    --card-white-edge: #f1f3f5;
    --ink-dark: #4a4d52;
    --ink-grey: #6d7177;
    --accent-blue: #3a9ad9;
    --mark-faint: #e6eef5;
    --back-blue-light: #27a5de;
    --back-blue-deep: #0a62a6;
    --back-name: #5a5d62;
  }
  * { margin: 0; padding: 0; box-sizing: border-box; }
  html, body {
    width: 1200px;
    height: 1023px;
    overflow: hidden;
    background: var(--stage);
  }
  .stage {
    position: relative;
    width: 1200px;
    height: 1023px;
  }
  .card {
    position: absolute;
    width: 600px;
    height: 343px;
    border-radius: 4px;
    box-shadow: 0 10px 26px rgba(0,0,0,0.18);
    overflow: hidden;
  }

  /* Front */
  .card--front {
    left: 90px;
    top: 120px;
    background: linear-gradient(160deg, var(--card-white) 55%, var(--card-white-edge));
  }
  .front__decor {
    position: absolute;
    right: 36px;
    top: 30px;
    width: 150px;
    height: 150px;
    background: var(--mark-faint);
  }
  .brand {
    position: absolute;
    left: 44px;
    top: 50px;
    display: flex;
    align-items: center;
    gap: 16px;
  }
  .brand__square {
    width: 54px;
    height: 54px;
    background: var(--accent-blue);
  }
  .brand__name {
    font-family: "Roboto", sans-serif;
    font-weight: 700;
    font-size: 30px;
    line-height: 1.05;
    color: var(--ink-dark);
  }
  .contact {
    position: absolute;
    left: 44px;
    top: 178px;
  }
  .contact__person {
    font-family: "Roboto", sans-serif;
    font-weight: 500;
    font-size: 24px;
    color: var(--accent-blue);
    margin-bottom: 14px;
  }
  .contact__line {
    display: flex;
    align-items: center;
    gap: 9px;
    font-family: "Open Sans", sans-serif;
    font-size: 15px;
    color: var(--ink-grey);
    margin-bottom: 6px;
  }
  .contact__icon {
    width: 14px;
    height: 14px;
    flex: none;
  }
  .contact__line--address { padding-left: 23px; margin-top: 6px; }

  /* Back */
  .card--back {
    left: 520px;
    top: 560px;
    background: radial-gradient(circle at 45% 35%, var(--back-blue-light), var(--back-blue-deep) 85%);
    display: flex;
    flex-direction: column;
    align-items: center;
    justify-content: center;
    gap: 18px;
  }
  .back__square {
    width: 70px;
    height: 70px;
    background: var(--card-white);
  }
  .back__name {
    font-family: "Roboto", sans-serif;
    font-weight: 700;
    font-size: 30px;
    color: var(--back-name);
  }
</style>
</head>
<body>
<main class="stage">
  <section class="card card--front" aria-label="Business card front">
    <div class="front__decor" aria-hidden="true"></div>
    <div class="brand">
      <div class="brand__square" aria-hidden="true"></div>
      <div class="brand__name">Hollowpine<br>Crafters LLC.</div>
    </div>
    <div class="contact">
      <p class="contact__person">Dale T.Voskuijl</p>
      <p class="contact__line">
        <svg class="contact__icon" viewBox="0 0 16 16" aria-hidden="true"><circle cx="8" cy="8" r="7.5" fill="#6d7177"/><path d="M5 4.5c.6-.4 1.2-.2 1.5.4l.5 1c.2.5 0 .9-.4 1.2.5 1 1.2 1.7 2.2 2.2.3-.4.7-.6 1.2-.4l1 .5c.6.3.8.9.4 1.5-.6.8-1.6 1-2.5.5C6.9 10.4 5.6 9.1 4.6 7.1c-.5-.9-.3-1.9.4-2.6z" fill="#fff"/></svg>
        406-738-1452
      </p>
      <p class="contact__line">
        <svg class="contact__icon" viewBox="0 0 16 16" aria-hidden="true"><rect x="1" y="3" width="14" height="10" rx="1" fill="#6d7177"/><path d="M1.5 3.8 8 9l6.5-5.2" fill="none" stroke="#fff" stroke-width="1.2"/></svg>
        dale@hollowpinecrafters.example
      </p>
      <p class="contact__line contact__line--address">4873 Quenwick dr. Colorado Springs, CO. 80462</p>
    </div>
  </section>

  <section class="card card--back" aria-label="Business card back">
    <div class="back__square" aria-hidden="true"></div>
    <p class="back__name">Hollowpine Crafters LLC.</p>
  </section>
</main>
</body>
</html>
```